Tessaline Bioscience Advisors.

Tessaline Bioscience Advisors. Feasibility, Evaluation and Validation of ISH/IHC and Imaging Applications.

Industry/Entity Type

Consulting

Contact Information for Business Card

Tessaline Bioscience Advisors
Cell: 330 555-0147
Dorian Makepeace
dmakepeace7804@quillmail.test

```html
<!DOCTYPE html>
<html lang="en">
<head>
<meta charset="utf-8">
<title>Tessaline Bioscience Advisors – Business Card</title>
<link rel="stylesheet" href="https://fonts.googleapis.com/css2?family=Roboto:wght@400;500;700&display=swap">
<style>
  :root {
    --backdrop: #d5d3d3;
    --paper: #ffffff;
    --brand-orange: #eb5d2a;
    --ink: #1a1a1a;
    --ink-soft: #333333;
  }
  * { box-sizing: border-box; margin: 0; padding: 0; }
  html, body { width: 1200px; height: 1000px; overflow: hidden; }
  body {
    background: var(--backdrop);
    font-family: "Roboto", Arial, sans-serif;
    position: relative;
  }
  .card {
    position: absolute;
    top: 345px;
    width: 525px;
    height: 310px;
    box-shadow: 0 6px 18px rgba(0,0,0,0.12);
  }
  /* Front side */
  .card-front { left: 50px; background: var(--paper); color: var(--ink); }
  .brand-lockup {
    position: absolute;
    top: 26px;
    right: 28px;
    display: flex;
    align-items: flex-end;
    gap: 8px;
  }
  .brand-square {
    width: 56px;
    height: 56px;
    background: var(--brand-orange);
  }
  .brand-name {
    font-size: 11px;
    font-weight: 500;
    line-height: 1.1;
    text-transform: uppercase;
    color: var(--ink);
    width: 96px;
  }
  .person {
    position: absolute;
    left: 30px;
    top: 150px;
  }
  .person-name { font-size: 17px; font-weight: 700; }
  .person-title {
    font-size: 7px;
    font-weight: 400;
    letter-spacing: 0.2px;
    text-transform: uppercase;
    margin-top: 2px;
  }
  .services {
    position: absolute;
    right: 28px;
    top: 112px;
    width: 250px;
    text-align: right;
    font-size: 9.5px;
    line-height: 1.35;
    color: var(--ink-soft);
  }
  .contact {
    position: absolute;
    right: 28px;
    top: 160px;
    text-align: right;
    font-size: 10px;
    font-weight: 700;
    line-height: 1.45;
  }
  /* Back side */
  .card-back {
    left: 625px;
    background: var(--brand-orange);
    color: var(--paper);
    display: flex;
    flex-direction: column;
    align-items: center;
    justify-content: center;
    gap: 12px;
  }
  .back-square {
    width: 104px;
    height: 104px;
    background: var(--paper);
  }
  .back-name {
    font-size: 19px;
    font-weight: 400;
    line-height: 1.1;
    text-transform: uppercase;
    text-align: center;
    width: 190px;
  }
</style>
</head>
<body>
  <section class="card card-front" aria-label="Business card front">
    <div class="brand-lockup">
      <div class="brand-square"></div>
      <p class="brand-name">Tessaline Bioscience Advisors</p>
    </div>
    <div class="person">
      <p class="person-name">Dorian Makepeace</p>
      <p class="person-title">Molecular Technology Consultant</p>
    </div>
    <p class="services">Feasibility, evaluation and validation of ish/ihc and imaging applications.</p>
    <div class="contact">
      <p>T: 330 555-0147</p>
      <p>E: dmakepeace7804@quillmail.test</p>
    </div>
  </section>

  <section class="card card-back" aria-label="Business card back">
    <div class="back-square"></div>
    <p class="back-name">Tessaline Bioscience Advisors</p>
  </section>
</body>
</html>
```